PDF-Dokumente für Vermietung und Verwaltung von Immobilien
Zielgruppe
WohnKranich, Vermietung und Verwaltung von Immoblien
Aufgabenstellung
Wir haben ganz viele Dokumente, die als PDF erstellt werden sollen, Einheitlich im CI Design, mit Logo etc. Manche PDFS müssen ausfüllbar sein andere sind einfach nur zum Drucken. es sind ca 10-20 Word/PDF Dokumente.

```html
<!DOCTYPE html>
<html lang="de">
<head>
<meta charset="utf-8">
<title>WohnKranich – Dokumentenreihe</title>
<link rel="stylesheet" href="https://fonts.googleapis.com/css2?family=Arimo:wght@400;700&family=Fira+Sans+Condensed:ital,wght@0,400;0,700;1,400&display=swap">
<style>
:root{
  --navy:#1e3350;
  --ink:#1f1f1f;
  --grey:#6b7078;
  --line:#9aa0a6;
  --green:#3f9a3a;
  --lime:#8cc63f;
  --orange:#f28a24;
  --blue:#24408e;
  --row:#e9e9e9;
  --badge:#d5d8dc;
}
html,body{margin:0;padding:0}
body{width:800px;height:1200px;overflow:hidden;background:#fff;position:relative;font-family:Arimo,Arial,sans-serif;color:var(--ink)}
.page{position:absolute;width:237px;height:336px;background:#fff;border:.6px solid #4a4a4a;box-sizing:border-box;overflow:hidden}
.band{position:absolute;left:0;right:0;bottom:0;height:4px;background:var(--navy)}
.band::after{content:"";position:absolute;left:76%;top:0;width:2px;height:100%;background:#fff;transform:skewX(-30deg)}
.brand{position:absolute;top:33px;left:8px;right:8px;display:flex;align-items:center;gap:5px}
.brand::before,.brand::after{content:"";flex:1;height:.6px;background:var(--line)}
.brand-mark{width:5px;height:5px;background:var(--grey)}
.brand-name{font-family:Arimo,Arial,sans-serif;font-size:5.6px;font-weight:400;color:var(--grey)}
.abs{position:absolute}
.title{left:0;right:0;text-align:center;font-weight:700;font-size:6px;line-height:7.5px}
.small{font-size:2.6px;line-height:3.4px}
.body{font-size:3.2px;line-height:4.2px}
.h{font-weight:700;font-size:4.8px}
.sec{font-weight:700;font-size:4.2px}
.ul{text-decoration:underline;font-size:3.6px;color:#1d2f6a}
.field{font-size:3.8px}
.rule{position:absolute;height:.5px;background:#555}
.cap{position:absolute;font-size:2.3px;font-weight:700}
.opt{position:absolute;left:14px;font-size:3.4px;line-height:4.2px}
.opt .box{display:inline-block;width:5px;height:5px;border:.5px solid #333;vertical-align:middle;margin-right:1px}
.opt ul{margin:0;padding-left:16px;font-size:2.5px;line-height:3.6px;list-style:circle}
.price{position:absolute;right:20px;font-size:3.2px}
.foot{position:absolute;left:22px;top:322px;font-size:3.1px;font-weight:700}
.sign{position:absolute;top:308px;left:22px;right:26px;border-top:.5px solid #555;font-size:3.2px;padding-top:1px}
.sign span{margin-left:66px}
.bar{position:absolute;left:24px;width:193px;top:66px;height:8px;background:var(--green);color:#fff;font-size:3.4px;display:flex;align-items:center}
.bar span{width:96px;padding-left:3px;box-sizing:border-box}
.ct-h{position:absolute;left:24px;font-size:2.8px;font-weight:700}
table.ct{position:absolute;left:24px;width:193px;border-collapse:collapse;font-size:2.3px}
table.ct td{border:.4px solid #777;background:var(--row);height:6.5px;padding:0 1.5px;line-height:2.6px}
table.ct td:nth-child(1){width:92px}
table.ct td:nth-child(2){width:70px}
table.ct td:nth-child(3){background:#d9d9d9}
table.ct td:nth-child(3)::after{content:"";display:block;width:4px;height:4px;background:#fff;margin:auto}
.note{position:absolute;left:25px;top:303px;width:62px;height:22px;border:.5px solid #555;font-size:2.5px;font-style:italic;text-align:center;display:flex;align-items:center;justify-content:center;padding:2px;box-sizing:border-box}
.gl{position:absolute;left:14px;font-size:3.3px;font-weight:700}
.gline{position:absolute;left:91px;width:131px;height:.5px;background:var(--lime)}
.contact{position:absolute;top:303px;font-family:"Times New Roman",serif;font-size:2.5px;line-height:3px;white-space:nowrap}
.q{position:absolute;font-family:"Fira Sans Condensed",Arial,sans-serif;font-size:3.5px;line-height:4.9px;color:#111;white-space:nowrap}
.q h4{margin:3px 0 0;font-size:3.6px;font-weight:700;color:var(--blue)}
.q h4.u{text-decoration:underline;font-size:3.8px}
.q .dot{display:inline-block;width:5px;height:5px;border-radius:50%;background:var(--orange);vertical-align:middle;margin-left:1px}
.q ul{list-style:none;margin:0;padding:0;color:var(--blue)}
.q li::before{content:"";display:inline-block;width:3px;height:3px;border:.4px solid #333;margin-right:1.5px;vertical-align:-.3px}
.q i{color:var(--blue)}
.q .ln{width:160px;height:.4px;background:#999;margin:3px 0}
.badge{position:absolute;left:165px;top:51px;width:52px;height:26px;background:var(--badge);border-radius:2px}
.grid{position:absolute;font-family:"Fira Sans Condensed",Arial,sans-serif;font-size:3.4px;line-height:6.2px;color:var(--blue)}
.grid b{color:#111}
.u2{display:inline-block;width:48px;border-bottom:.4px solid #555}
</style>
</head>
<body>

<section class="page" style="left:51px;top:75px">
  <div class="brand"><span class="brand-mark"></span><span class="brand-name">WohnKranich</span></div>
  <div class="abs h" style="left:70px;top:52px">Kurzgutachten – Wertermittlung</div>
  <div class="abs" style="left:28px;top:72px;width:190px">
    <div class="sec">1. Umfang des Kurzgutachtens</div>
    <p class="body" style="margin:1px 0">Das Kurzgutachten umfasst eine Beschreibung der Objekt- und Lagedaten. Die Wertermittlung erfolgt nach normierten Verfahren statt und wird entsprechend der Marktlage berücksichtigt. Rechtliche und tatsächliche Rechte und Lasten werden erfasst und eine Fotodokumentation vorgenommen. Zusätzlich wird ein Bodenrichtwertauszug, sowie ein Grundbuchauszug eingeholt und zugrundegelegt.</p>
  </div>
  <div class="abs" style="left:28px;top:136px;width:190px">
    <div class="sec">2. Verwendung</div>
    <p class="body" style="margin:1px 0">Das Kurzgutachten ist sinnvoll, wenn Sie mit einem überschaubaren Kostenrahmen den Wert oder den Verkauf innerhalb der Familie planen, bei außergerichtlichen Auseinandersetzungen und Trennungen. Weiterhin ist ein Kurzgutachten eine gute Grundlage und eignet sich somit nicht für gerichtliche Verfahren.</p>
  </div>
  <div class="abs" style="left:28px;top:196px;width:190px">
    <div class="sec">3. Unterschied zum Verkehrswertgutachten</div>
    <p class="body" style="margin:1px 0">Das Kurzgutachten ist deutlich verkürzt gegenüber (§ 194 BauGB). Es werden keine behördlichen Auskünfte und die Lageschreibung verkürzt. Das Kurzgutachten dient der Wertermittlung und das Ergebnis ist allein für den Auftraggebers, das Grundbuch, die Unterlagen, der Ortstermin, sowie die im Grundstücksmarkt.</p>
  </div>
  <div class="abs" style="left:28px;top:247px;width:190px">
    <div class="sec">4. Vorteile des Kurzgutachtens</div>
    <p class="body" style="margin:1px 0">- Schnelle zeitnahe Erstellung und Auslieferung<br>- Kurzgutachten zum Festpreis ab 300 €<br>- Schriftliche Dokumentation des Marktwertes<br>- Werteinschätzung als Entscheidungshilfe<br>- Plausibilisierung von Exposédaten<br>- TÜV-zertifizierter Gutachter</p>
  </div>
  <div class="abs h" style="left:28px;top:302px;font-size:5.2px">Für Fragen rufen Sie uns an</div>
  <div class="abs" style="left:28px;top:313px;font-size:3px;font-weight:700">Weitere Informationen finden Sie online</div>
  <div class="foot" style="left:28px">WohnKranich GmbH, Kranichweg</div>
  <div class="band"></div>
</section>

<section class="page" style="left:140px;top:75px">
  <div class="brand"><span class="brand-mark"></span><span class="brand-name">WohnKranich</span></div>
  <div class="abs title" style="top:51px">Auftrag<br>Kurzgutachten / Wertermittlung</div>
  <div class="abs field" style="left:28px;top:76px">Objekt:</div>
  <div class="rule" style="left:66px;right:36px;top:82px"></div>
  <div class="cap" style="left:68px;top:83.5px">Anschrift (Straße, PLZ, Ort)</div>
  <div class="abs field" style="left:28px;top:90px">Auftraggeber/in:</div>
  <div class="rule" style="left:66px;right:36px;top:96px"></div>
  <div class="cap" style="left:68px;top:97.5px">Name, Vorname</div>
  <div class="rule" style="left:66px;right:36px;top:110px"></div>
  <div class="cap" style="left:68px;top:111.5px">Anschrift (Straße, PLZ, Ort)</div>
  <div class="rule" style="left:66px;right:36px;top:123px"></div>
  <div class="cap" style="left:68px;top:124.5px">Telefonnummer, E-Mail</div>
  <div class="abs" style="left:28px;top:134px;font-size:2.6px">(bitte ankreuzen)</div>
  <div class="opt" style="top:140px"><span class="box"></span>Kurzgutachten / Wertermittlung Eigentumswohnung
    <ul><li>Ortstermin inkl. Unterlagensichtung</li><li>Einholung des Grundbuches, Liegenschaftskarte und Bodenrichtwert</li><li>Berechnung und Wertermittlung mittels normierter Verfahren</li><li>Fotodokumentation</li><li>Schriftliche Ausfertigung</li></ul></div>
  <div class="price" style="top:170px">300,00 € inkl. MwSt.</div>
  <div class="opt" style="top:180px"><span class="box"></span>Kurzgutachten / Wertermittlung Einfamilienhaus<ul><li>Leistungen wie oben angegeben.</li></ul></div>
  <div class="price" style="top:190px">400,00 € inkl. MwSt.</div>
  <div class="opt" style="top:199px"><span class="box"></span>Kurzgutachten / Wertermittlung Mehrfamilienhaus<ul><li>Leistungen wie oben angegeben.</li></ul></div>
  <div class="price" style="top:210px">500,00 € inkl. MwSt.</div>
  <div class="opt" style="top:219px"><span class="box"></span>Kurzgutachten / Wertermittlung Haus mit Nebengebäuden<ul><li>Leistungen wie oben angegeben.</li></ul></div>
  <div class="price" style="top:230px">600,00 € inkl. MwSt.</div>
  <p class="abs small" style="left:28px;right:28px;top:241px;margin:0;text-align:justify">Ich beauftrage die Immobilienberatung Weserland GmbH mit den angekreuzten Leistungen. Die Zahlung des Honorars ist fällig mit Rechnungstellung und Übergabe des Kurzgutachtens. Rechtliche Genehmigungen, behördliche Auskünfte sowie die vom Auftraggeber zur Verfügung gestellten Unterlagen werden nicht überprüft. Die Maße und Angaben werden vom Eigentümer übernommen. Im Zweifel findet eine Schätzung statt. Das Kurzgutachten stellt kein Verkehrswertgutachten gem. § 194 BauGB dar. Das Urheberrecht liegt beim Gutachtenersteller. Das Kurzgutachten dient ausschließlich der Einschätzung des voraussichtlich in einer Immobilie zu erzielenden Marktpreises und unterscheidet sich insofern von einem formalen Gutachten. Für etwaige Abweichungen von ggf. tatsächlich erzielten Kauf- und / oder Verkaufspreisen und / oder Werten wird jedwede Haftung ausgeschlossen. Insgesamt ist die Haftung auf Vorsatz und grobe Fahrlässigkeit und auf den Betrag begrenzt, der für die Erstellung desselben erhoben wird.</p>
  <div class="sign">Ort, Datum<span>Unterschrift Auftraggeber/in</span></div>
  <div class="foot">WohnKranich GmbH, Kranichweg 16, 28199 Musterstadt</div>
  <div class="band"></div>
</section>

<section class="page" style="left:432px;top:75px">
  <div class="brand"><span class="brand-mark"></span><span class="brand-name">WohnKranich</span></div>
  <div class="abs h" style="left:60px;top:52px">Qualifizierte Wohnflächenberechnung</div>
  <div class="abs" style="left:28px;top:77px;width:190px">
    <div class="ul">Qualifizierte Wohnflächenberechnung</div>
    <p class="body" style="margin:1px 0">Die Wohnfläche bezeichnet die Grundfläche der Räume, die ausschließlich zu einer Wohnung gehören. Eine genaue Angabe der Wohnfläche in m² ist für viele Fragen wichtig. Liegen keine Grundrisse und genaue Angaben vor, wird das Ergebnis wird qualifiziert dokumentiert und dient für Immobilienfinanzierungen. Ebenfalls für die Prüfung der Richtigkeit Ihres Mietvertrags sowie Nebenkosten.</p>
  </div>
  <div class="abs" style="left:28px;top:131px;width:190px">
    <div class="ul">Die Wohnflächenverordnung (WoFlV)</div>
    <p class="body" style="margin:1px 0">Die Wohnflächenverordnung findet Anwendung beim Wohnraum regelmäßig Anwendung für die Wohnflächenbestimmung. Die Verordnung regelt, wie Besondere Flächen wie Terrassen und Balkone mit Abschlägen angerechnet.</p>
  </div>
  <div class="abs" style="left:28px;top:176px;width:190px">
    <div class="ul">Leistungsumfang einer Wohnflächenberechnung</div>
    <p class="body" style="margin:1px 0">o Ortstermin inkl. Aufmaß und Unterlagensichtung<br>o Berechnung der Wohnfläche gem. WoFlV<br>o Dokumentation der Berechnung<br>o Ausweisung der Wohnfläche gem. WoFlV</p>
  </div>
  <div class="abs" style="left:28px;top:216px;width:190px">
    <div class="ul">Ergebnis der Wohnflächenberechnung</div>
    <p class="body" style="margin:1px 0">Die Besichtigung und das Aufmaß dauern, die Bearbeitung beträgt nach dem Ortstermin in der Regel wenige Werktage, in besonders eiligen Fällen ist ein Express möglich.</p>
  </div>
  <div class="abs" style="left:28px;top:251px;width:190px">
    <div class="ul">Ihre Vorteile</div>
    <p class="body" style="margin:1px 0 0 6px">-&nbsp;&nbsp; Zeitnahe Auftragsbearbeitung<br>-&nbsp;&nbsp; Präzise Messung der Flächen vor Ort<br>-&nbsp;&nbsp; Flächenberechnung nach WoFlV<br>-&nbsp;&nbsp; Schriftlicher Bericht mit tabellarischer Übersicht<br>-&nbsp;&nbsp; Festpreis<br>-&nbsp;&nbsp; TÜV zertifizierter Gutachter</p>
  </div>
  <div class="abs h" style="left:28px;top:302px;font-size:5.2px">Für Fragen rufen Sie uns an</div>
  <div class="abs" style="left:28px;top:313px;font-size:3px;font-weight:700">Weitere Informationen finden Sie online</div>
  <div class="foot" style="left:28px">WohnKranich GmbH, Kranichweg</div>
  <div class="band"></div>
</section>

<section class="page" style="left:520px;top:75px">
  <div class="brand"><span class="brand-mark"></span><span class="brand-name">WohnKranich</span></div>
  <div class="abs title" style="top:51px">Auftrag<br>Kurzgutachten / Wertermittlung</div>
  <div class="abs field" style="left:28px;top:74px">Objekt:</div>
  <div class="rule" style="left:66px;right:36px;top:80px"></div>
  <div class="cap" style="left:68px;top:81.5px">Anschrift (Straße, PLZ, Ort)</div>
  <div class="abs field" style="left:28px;top:88px">Auftraggeber/in:</div>
  <div class="rule" style="left:66px;right:36px;top:94px"></div>
  <div class="cap" style="left:68px;top:95.5px">Name, Vorname</div>
  <div class="rule" style="left:66px;right:36px;top:108px"></div>
  <div class="cap" style="left:68px;top:109.5px">Anschrift (Straße, PLZ, Ort)</div>
  <div class="rule" style="left:66px;right:36px;top:121px"></div>
  <div class="cap" style="left:68px;top:122.5px">Telefonnummer, E-Mail</div>
  <div class="abs" style="left:28px;top:132px;font-size:2.6px">(bitte ankreuzen)</div>
  <div class="opt" style="top:139px"><span class="box"></span>Wohnflächenberechnung Standard bis 100 m²
    <ul><li>Ortstermin inkl. Aufmaß und Unterlagensichtung</li><li>Berechnung der Wohnfläche gem. WoFlV</li><li>Dokumentation der Berechnung</li><li>Ausweisung der Wohnfläche gem. WoFlV</li></ul></div>
  <div class="price" style="top:165px">300,00 € inkl. MwSt.</div>
  <div class="opt" style="top:174px"><span class="box"></span>Wohnflächenberechnung Standard bis 150 m²<ul><li>Leistungen wie oben angegeben.</li></ul></div>
  <div class="price" style="top:185px">400,00 € inkl. MwSt.</div>
  <div class="opt" style="top:194px"><span class="box"></span>Wohnflächenberechnung Standard bis 200 m²<ul><li>Leistungen wie oben angegeben.</li></ul></div>
  <div class="price" style="top:205px">475,00 € inkl. MwSt.</div>
  <div class="opt" style="top:214px"><span class="box"></span>Wohnflächenberechnung Standard über 200 m²<ul><li>Leistungen wie oben angegeben.</li></ul></div>
  <div class="price" style="top:225px">550,00 € inkl. MwSt.</div>
  <div class="opt" style="top:234px"><span class="box"></span>Bilderdokumentation des Objekts<ul><li>Objektbilder Innen und Außen</li></ul></div>
  <div class="price" style="top:245px">50,00 € inkl. MwSt.</div>
  <div class="opt" style="top:254px"><span class="box"></span>Grundrisse inkl. Innenmaße (1/100)</div>
  <div class="price" style="top:260px">200,00 € inkl. MwSt.</div>
  <p class="abs small" style="left:28px;right:28px;top:268px;margin:0;text-align:justify">Ich beauftrage die Immobilienberatung Weserland GmbH mit den angekreuzten Leistungen. Die Messtoleranz und Abweichung kann bis zu 1,5 % bei Aufmaß und Berechnung betragen. Die Zahlung des Honorars ist fällig mit Rechnungstellung und Übergabe der Wohnflächenberechnung. Bei grober Fahrlässigkeit ist die Haftung begrenzt auf eine Haftungssumme in Höhe von 5.000,00 €. Rechtliche Genehmigungen oder tatsächliche Mängel oder Schäden werden nicht geprüft. Eine Beratung findet nicht statt.</p>
  <div class="sign" style="top:311px">Ort, Datum<span>Unterschrift Auftraggeber/in</span></div>
  <div class="foot" style="top:323px">WohnKranich GmbH, Kranichweg 16, 28199 Musterstadt</div>
  <div class="band"></div>
</section>

<section class="page" style="left:148px;top:457px">
  <div class="brand"><span class="brand-mark"></span><span class="brand-name">WohnKranich</span></div>
  <div class="abs title" style="top:52px;font-weight:400;font-size:5.2px">Checkliste Unterlagen</div>
  <div class="bar"><span>Was wird für ein Gutachten benötigt ?</span><span>Woher bekomme ich die Unterlagen ?</span></div>
  <div class="ct-h" style="top:84px">Bauunterlagen und Genehmigungen</div>
  <table class="ct" style="top:91px">
    <tr><td>Grundbuchauszug</td><td>Grundbuchamt (Amtsgericht)</td><td></td></tr>
    <tr><td>Flurkarte (Lageplan)</td><td>Katasteramt (Bauamt)</td><td></td></tr>
    <tr><td>Baulastenauskunft</td><td>Baulastenverzeichnis (Bauamt)</td><td></td></tr>
    <tr><td>Wohnflächen- und Nutzflächenberechnung (Quadratmeter)</td><td>Genehmigte Baupläne, Bauakte (Bauamt)</td><td></td></tr>
    <tr><td>Grundrisspläne von allen Geschossen (auch Keller)</td><td>Genehmigte Baupläne, Bauakte (Bauamt)</td><td></td></tr>
    <tr><td>Schnitte von allen Geschossen</td><td>Genehmigte Baupläne, Bauakte (Bauamt)</td><td></td></tr>
    <tr><td>Ansichten</td><td>Genehmigte Baupläne, Bauakte (Bauamt)</td><td></td></tr>
    <tr><td>Schlussabnahmeschein (Bauabnahme)</td><td>Genehmigte Baupläne, Bauakte (Bauamt)</td><td></td></tr>
    <tr><td>Bei Sanierung oder Anbau: Jahr und Kostenaufwand, zusätzlich genehmigte Bauunterlagen und Schlussabnahmeschein</td><td>Genehmigte Baupläne, Bauakte (Bauamt)</td><td></td></tr>
  </table>
  <div class="ct-h" style="top:165px">Bei Wohnungseigentum</div>
  <table class="ct" style="top:172px">
    <tr><td>Teilungserklärung (bei Wohnungseigentum)</td><td>Verwalter/Grundakte (Grundbuchamt) oder Kaufvertrag</td><td></td></tr>
    <tr><td>Bezeichnung des Wohnungseigentums (z.B. Whg. Nr. 5)</td><td>Teilungserklärung/Grundbuchauszug/oder Kaufvertrag/ Grundakte (Grundbuchamt)</td><td></td></tr>
    <tr><td>Anschrift des Verwalters</td><td>Letzte Abrechnung</td><td></td></tr>
    <tr><td>Aktuelles Hausgeld</td><td>Verwalter/Abrechnung</td><td></td></tr>
    <tr><td>Die letzten 3 Protokolle der Versammlung</td><td>Verwalter/eigene Unterlagen</td><td></td></tr>
    <tr><td>Energieausweis</td><td>Verwalter/eigene Unterlagen</td><td></td></tr>
  </table>
  <div class="ct-h" style="top:224px">Bei Grundbuch eingetragene Rechte</div>
  <table class="ct" style="top:231px">
    <tr><td>Zum Beispiel: Erbbaurecht / Wegerechte / Dienstbarkeiten / Leitungsrechte / Rentenrechte</td><td>Grundakte (Grundbuchamt) Ursprünglicher Notarvertrag in Ihren eigenen Unterlagen</td><td></td></tr>
  </table>
  <div class="ct-h" style="top:247px">Sonstiges</div>
  <table class="ct" style="top:254px">
    <tr><td>Bei vermieteten Objekten: Mietverträge und letzte Mieterhöhungsschreiben, Kontaktdaten der Mieter.</td><td>Aus Ihren Unterlagen</td><td></td></tr>
    <tr><td>Energieausweis</td><td>Aus Ihren Unterlagen</td><td></td></tr>
    <tr><td>Falls Sie als Betreuer durch das Gericht bestellt sind: Gerichtliche Bestellungsurkunde.</td><td>Aus Ihren Unterlagen</td><td></td></tr>
    <tr><td>Vollmacht zu Akteneinsicht beim Bauamt und Grundbuchamt</td><td>Aus dem Auftrag als Vordruck</td><td></td></tr>
    <tr><td>Mieteraufstellung (Mietverträge)</td><td>Aus Ihren Unterlagen</td><td></td></tr>
  </table>
  <div class="note">Bitte senden Sie uns die benötigten Unterlagen möglichst vor dem Ortstermin in Kopie zu.</div>
  <div class="abs" style="left:106px;top:314px;font-size:3.2px;font-weight:700">Ort; Datum:</div>
  <div class="abs" style="left:132px;top:311px;font-size:6px">X</div>
  <div class="rule" style="left:132px;width:72px;top:318px"></div>
  <div class="band"></div>
</section>

<section class="page" style="left:422px;top:457px">
  <div class="brand" style="top:35px"><span class="brand-mark"></span><span class="brand-name">WohnKranich</span></div>
  <div class="abs title" style="top:53px;font-size:3.6px;line-height:4.6px;letter-spacing:.8px">BÜRGSCHAFTSURKUNDE</div>
  <div class="abs title" style="top:58px;font-size:3.2px">für das Mietverhältnis</div>
  <div class="gl" style="top:80px">zwischen dem Vermieter</div>
  <div class="gline" style="top:84px"></div><div class="gline" style="top:93px"></div>
  <div class="gl" style="top:107px">und dem Mieter</div>
  <div class="gline" style="top:111px"></div><div class="gline" style="top:120px"></div>
  <div class="gl" style="top:133px">für das Mietobjekt</div>
  <div class="gline" style="top:137px"></div>
  <div class="gl" style="top:151px">Hiermit übernehme ich</div>
  <div class="gl" style="top:166px">Vorname, Nachname</div><div class="gline" style="top:170px"></div>
  <div class="gl" style="top:175px">Anschrift:</div><div class="gline" style="top:179px"></div>
  <div class="gl" style="top:184px">Geboren am, in</div><div class="gline" style="top:188px"></div>
  <div class="abs" style="left:14px;right:14px;top:200px;font-size:3.1px;line-height:4.6px;font-weight:700">
    <p style="margin:0 0 3px">die unbefristete, freiwillige und selbstschuldnerische Bürgschaft für den o. g. Mieter in dem o. g. Mietverhältnis.</p>
    <p style="margin:0 0 3px">Die Bürgschaft gilt für alle Mietzinsansprüche, Nachzahlung von Betriebskosten aus der jeweiligen Abrechnung und einer evtl. stillschweigenden Verlängerung des Mietverhältnisses. Bei dieser Bürgschaft handelt es sich um eine freiwillige, selbstschuldnerische Bürgschaft, die die Zahlung einer Mietkaution nicht ersetzt. Die Bürgschaft gilt über die Kündigung, gemäß § 568 BGB, hinaus.</p>
    <p style="margin:0 0 3px">Ich verzichte ausdrücklich auf mir nach dem Gesetz zustehende Einreden, insbesondere auf die Einrede der Anfechtung, der Aufrechnung und der Vorausklage und der Hinterlegung gemäß §§ 770, 771 BGB.</p>
    <p style="margin:0">Dieser Bürgschaftsurkunde lege ich eine Kopie meines Personalausweises bei.</p>
  </div>
  <div class="abs" style="left:14px;width:74px;top:283px;height:.5px;background:var(--lime)"></div>
  <div class="abs" style="left:113px;width:109px;top:283px;height:.5px;background:var(--lime)"></div>
  <div class="gl" style="top:288px">Ort, Datum</div>
  <div class="gl" style="left:113px;top:288px">Unterschrift des Bürgen</div>
  <div class="abs" style="left:12px;right:10px;top:301px;height:.8px;background:var(--navy)"></div>
  <div class="contact" style="left:14px">● WohnKranich GmbH<br>&nbsp;&nbsp;Kranichweg 16<br>&nbsp;&nbsp;28199 Musterstadt</div>
  <div class="contact" style="left:66px">☎ 0421 5550123<br>✉ info@wohnkranich.de<br>⊕ www.wohnkranich.de</div>
  <div class="contact" style="left:110px">■ Bankverbindung:<br>&nbsp;&nbsp;Musterbank Nord<br>&nbsp;&nbsp;IBAN: DE00 1234 5678 0000 0000 00<br>&nbsp;&nbsp;BIC: MUSTDE2XXXX</div>
  <div class="contact" style="left:180px">▲ Geschäftsführer:<br>&nbsp;&nbsp;Jana Berg &amp; Timo Wendt<br>&nbsp;&nbsp;USt-ID-Nr.: DE000000000<br>&nbsp;&nbsp;HRB 00000 HB</div>
  <div class="band" style="height:13px"></div>
</section>

<section class="page" style="left:51px;top:831px">
  <div class="brand"><span class="brand-mark"></span><span class="brand-name">WohnKranich</span></div>
  <div class="q" style="left:32px;top:54px">
    <h4 class="u">Lage und Umgebung<span class="dot"></span></h4>
    <h4>Grundstücksform</h4>
    <ul><li>Rechteckig</li><li>Trapezförmig</li></ul>
    <div style="height:24px"></div>
    <h4>Strahlung</h4>
    <ul><li>Hochspannungsmast in der Nähe</li><li>Mobilfunkantenne in der Nähe</li></ul>
    <h4>Lärm</h4>
    <ul><li>Industrie</li><li>Glockenturm in der Nähe</li><li>Starker Straßenverkehr</li><li>Kindergarten/Schule <span style="font-size:2.4px">(wenn als Störung empfunden)</span></li></ul>
    <h4>Ortslage</h4>
    <ul><li>Ortskern/Innenstadt</li><li>Ortsrand/Vorort</li><li>Wohngebiet</li><li>Wohn- und Geschäftsgebiet</li><li>Gewerbegebiet</li><li>Ländliches Mischgebiet</li><li>Waldrand oder Alleinlage</li></ul>
    <h4>Eindruck Nachbarschaft:</h4>
    <div class="ln"></div><div class="ln"></div>
    <h4 class="u">Objekt von außen<span class="dot"></span></h4>
    <h4>Zufahrt/Straße</h4>
    <ul><li>Asphaltiert</li><li>Gepflastert</li><li>Teerbelag</li><li>Holzbelag</li><li>Nicht befestigt</li></ul>
    <h4>Bepflanzung</h4>
    <ul><li>Keine</li><li>Rasen</li><li>Blumenbeete</li><li>Sträucher</li><li>Bäume ___ Anzahl</li></ul>
    <h4>Dacheindeckung<span class="dot"></span></h4>
    <ul><li>Schiefer</li><li>Tondachpfannen</li><li>Metallblech</li><li>Betondachpfannen</li><li>Bitumen</li></ul>
  </div>
  <div class="band"></div>
</section>

<section class="page" style="left:168px;top:831px">
  <div class="brand"><span class="brand-mark"></span><span class="brand-name">WohnKranich</span></div>
  <div class="q" style="left:36px;top:52px">
    <h4>Objektart<span class="dot"></span></h4>
    <ul><li>Einfamilienhaus</li><li>Doppelhaushälfte</li><li>Reihenendhaus</li><li>Reihenmittelhaus</li></ul>
    <h4>Dämmung<span class="dot"></span></h4>
    <ul><li>Außendämmung</li><li>Innendämmung</li><li><i>Mauerdicke (&gt;38cm)</i></li></ul>
    <h4 class="u">Ausstattung<span class="dot"></span></h4>
    <h4>Verkabelung</h4>
    <ul><li>Unterputz</li><li>Aufputz</li></ul>
    <h4>Innentüren<span class="dot"></span></h4>
    <ul><li>Massivholz</li><li>Ganzglas</li><li>Standard</li><li>Holz-/Kunststofffurniert</li><li>Glaseinsatz</li><li>Holzzarge</li><li>Stahlzarge</li><li>Einfach/minderwertig</li></ul>
    <h4>Fenster<span class="dot"></span></h4>
    <ul><li>Kunststoff</li><li>Aluminium</li><li>Holz</li><li>Doppelfenster/Kastenfenster</li><li>Wärmeschutzverglast</li><li>Isolierverglast</li><li>Einfachverglast</li><li>Markise/Sonnenschutz</li><li>Funktionstüchtigkeit</li></ul>
    <h4>TV-Anschluss</h4>
    <ul><li>Antenne/Kabel</li><li>Satellit</li></ul>
    <h4 class="u">Küche</h4>
    <h4>Ausstattung</h4>
    <ul><li>Anschluss Waschmaschine vorhanden</li><li>Einbaugeräte</li></ul>
    <div style="height:18px"></div>
    <h4>Welche Einbauten werden mit Kauf übergeben?</h4>
    <div class="ln"></div><div class="ln"></div><div class="ln"></div>
  </div>
  <div class="band"></div>
</section>

<section class="page" style="left:286px;top:831px">
  <div class="brand"><span class="brand-mark"></span><span class="brand-name">WohnKranich</span></div>
  <div class="q" style="left:40px;top:52px;line-height:4.75px">
    <h4 class="u">Bad &amp; WC</h4>
    <h4>Ausstattungsgegenstände<span class="dot"></span></h4>
    <ul><li>Badewanne</li><li>Duschkabine</li><li>Waschtischanlage</li><li>Einzelwaschbecken</li><li>Bidet</li><li>Pissoir</li><li>Modern/Hochwertig</li><li>Standardausführung</li><li>Veraltet/sehr einfach</li></ul>
    <h4>Zustand und Anschlüsse</h4>
    <ul><li>Fliesen &amp; Fugen Zustand O.K.</li><li>Bodenbelag O.K.</li><li>Armaturen O.K.</li><li>Silikondichtungen O.K.</li><li>Waschmaschinenanschluss vorhanden</li></ul>
    <div style="height:8px"></div>
    <h4>Heizungsinstallation, <i>Alter __Jahre, Letzte Wartung</i></h4>
    <ul><li>Modern, mit alternativer Energieversorgung</li><li>Modern, mit Standard-Energieversorgung</li><li>Öl-/Gasetagenheizung mit Standardbrenner</li><li>Einfache Ölheizung mit veraltetem Brenner</li><li>Veraltete Einzelöfen (Öl oder Holz)</li><li>Nachtspeicheröfen</li><li>Fußbodenheizung in den Wohnräumen</li><li>Fußbodenheizung in den Bädern</li><li>Stahlradiatoren</li><li>Plattenheizkörper</li></ul>
    <h4>Keller</h4>
    <ul><li><i>Im Keller feuchte Wände</i></li></ul>
    <h4>Unterlagen liegen vor</h4>
    <ul><li>evtl. Sachverständigengutachten</li><li>Lageplan &amp; Flurstücksnummer</li><li>Grundbuchauszug</li><li>Schornsteinfegerprotokolle</li></ul>
    <h4>Frühere Schäden und Schädlingsbefall am Objekt</h4>
    <ul><li>Schimmel</li><li>Feuchtigkeitsschäden</li></ul>
    <h4 class="u">Weitere Faktoren</h4>
    <h4>Raumaufteilung<span class="dot"></span></h4>
    <ul><li>Sehr große Räume</li><li>Große Räume, gut geschnitten, gutes Verhältnis</li><li>Räume von normaler Größe</li><li>Kleine Räume, ungünstig geschnitten, Durchgangszimmer</li><li>Sehr kleine Räume</li><li>Räume teilweise nicht nutzbar</li></ul>
  </div>
  <div class="band"></div>
</section>

<section class="page" style="left:403px;top:831px">
  <div class="brand"><span class="brand-mark"></span><span class="brand-name">WohnKranich</span></div>
  <div class="q" style="left:30px;top:54px">
    <h4>Besonnung/Belichtung<span class="dot"></span></h4>
    <ul><li>Sehr helle Räume, großzügige Fensterflächen</li><li>Helle Räume</li><li>Räume sind weder besonders hell noch besonders dunkel</li><li>Sehr dunkle Räume, teilweise ohne Fenster</li></ul>
    <h4>Aussicht<span class="dot"></span></h4>
    <ul><li>Berg- oder Seeblick</li><li>Blick auf Grünanlagen</li><li>Typisch für Lage und Umgebung</li></ul>
    <h4 class="u">Renovierungs- und Sanierungsmaßnahmen</h4>
    <h4>Wand- und Bodenbeläge _____ <i>(Jahr)</i></h4>
    <h4><i>Erneuerung Bodenbeläge und Malerarbeiten</i></h4>
    <ul><li>In allen Räumen</li><li>In fast allen Räumen</li></ul>
    <h4>Bad &amp; WC _____ <i>(Jahr)</i></h4>
    <h4><i>Erneuerung</i></h4>
    <ul><li>Sanitärgegenstände</li><li>Armaturen</li></ul>
    <h4>Heizung &amp; Warmwasseraufbereitung &amp; Wasserleitungen</h4>
    <h4><i>Erneuerung</i></h4>
    <ul><li>Brenner</li><li>Boiler</li></ul>
    <h4>Fassade &amp; Fenster _____ <i>(Jahr)</i></h4>
    <h4><i>Erneuerung</i></h4>
    <ul><li>Fenster</li><li>Fassade</li></ul>
    <h4>Dach _____ <i>(Jahr)</i></h4>
    <ul><li>Dacherneuerung komplett inkl. Dämmung und Eindeckung</li><li>Erneuerung Dämmung und Eindeckung ohne Konstruktion</li></ul>
    <h4>Welche Renovierungs-/Sanierungsarbeiten sind geplant?</h4>
    <div style="height:4px"></div>
    <h4>Gewerk &amp; Zeitpunkt</h4>
    <div class="ln"></div><div class="ln"></div><div class="ln"></div>
    <h4>Weitere Notizen:</h4>
    <div class="ln"></div><div class="ln"></div>
  </div>
  <div class="band"></div>
</section>

<section class="page" style="left:520px;top:831px">
  <div class="brand"><span class="brand-mark"></span><span class="brand-name">WohnKranich</span></div>
  <div class="badge" role="img" aria-label="Platz für Partnerplakette"></div>
  <div class="q" style="left:28px;top:86px;white-space:normal;width:185px;line-height:4.6px">
    <div style="font-weight:700;font-size:4.8px;color:var(--blue)">Immobilienbewertung leicht gemacht.</div>
    <div style="margin-top:2px">1.&nbsp;&nbsp; Füllen Sie einfach diesen Fragebogen bei der Hausbesichtigung aus.</div>
    <div>2.&nbsp;&nbsp; Geben Sie die Kriterien unter <span style="color:var(--blue);text-decoration:underline">www.wohnwertportal.de/bewertung</span> ein.</div>
    <div>3.&nbsp;&nbsp; Nach den Zahlungsmodalitäten erhalten Sie sofort Ihre Immobilienbewertung im PDF-Format.</div>
    <div style="font-size:2.6px;line-height:3.4px;margin-top:2px;color:var(--blue)"><b>Hinweis:</b> Im Folgenden finden Sie eine Checkliste aller Dinge, die für eine Hausbesichtigung beachtenswert sind. Trotz des umfangreichen Fragenkatalogs übernehmen wir keine Haftung für dessen Vollständigkeit und weisen darauf hin, dass es wertbeeinflussende Merkmale am Objekt geben kann, die hier nicht enthalten sind.</div>
    <div style="font-size:2.8px;margin-top:2px;color:var(--blue)"><span class="dot"></span> Tipp: Die orange markierten Punkte sind für eine Online-Immobilienbewertung wichtig.</div>
  </div>
  <div class="q" style="left:28px;top:152px">
    <h4 class="u">Basisinformationen<span class="dot"></span></h4>
  </div>
  <div class="grid" style="left:28px;top:164px">
    <b>Anschrift</b><br>
    Straße, Hausnr. <span class="u2" style="margin-left:22px;width:64px"></span><br>
    Postleitzahl, Ort <span class="u2" style="margin-left:20px;width:64px"></span>
  </div>
  <div class="grid" style="left:138px;top:170px"><b>Besichtigt am:</b> <span class="u2" style="width:22px"></span><br><b>Angebotspreis:</b> <span class="u2" style="width:22px"></span> €</div>
  <div class="grid" style="left:28px;top:196px"><b>Eigentümer</b><br>Name <span class="u2" style="margin-left:38px;width:46px"></span><br>Telefon <span class="u2" style="margin-left:34px;width:46px"></span><br>Gründe Verkauf <span class="u2" style="margin-left:17px;width:46px"></span></div>
  <div class="grid" style="left:120px;top:196px"><b>Makler</b><br>Name <span class="u2" style="margin-left:24px;width:46px"></span><br>Telefon <span class="u2" style="margin-left:20px;width:46px"></span><br>E-Mail <span class="u2" style="margin-left:22px;width:46px"></span></div>
  <div class="grid" style="left:28px;top:237px">
    Baujahr<br>Wohnfläche<br>Grundstücksfläche<br>Balkon<br>Terrasse<br>(Tief)Garage/Carport
  </div>
  <div class="grid" style="left:80px;top:237px">
    <span class="u2" style="width:12px"></span><br><span class="u2" style="width:12px"></span> m²<br><span class="u2" style="width:12px"></span> m²<br><span class="u2" style="width:12px"></span> m²<br><span class="u2" style="width:12px"></span> m²<br><span class="u2" style="width:12px"></span> (Anzahl)
  </div>
  <div class="q" style="left:120px;top:237px;line-height:6.2px;font-size:3.4px">
    <ul><li>Das Objekt ist vermietet?</li><li style="margin-left:8px"><i>Mietvertrag vorhanden</i></li><li>Erschließungskosten bezahlt</li><li style="list-style:none">&nbsp;&nbsp;&nbsp;(Wasser-/Stromanschluss etc.)</li><li>Weitere Erschließung geplant/erforderlich</li><li>Unterkellert</li></ul>
  </div>
  <div class="band"></div>
</section>

</body>
</html>
```